Real Estate Development Sign

I am trying to get some good graphic design help for a new real estate development project. We need two designs for two separate large billboard-type directionals, also For Sale Signs, and also bandit directional signs. I have a company who have already given it a shot, but I don't like what they have come up with. I need it to have a WOW factor and pop to catch people's eye, but also simple and easy to read. I've attached what they have done so far. I have proofs of what has already been created and I've attached them. I've also attached the logo for the project, but I'm fine with changing the color for the logo to help make the overall signs more cohesive. I want clean, easy to read and eye catching. I will need to be able to pass the designs on to a company to have them printed for the billboards. One of them is 10x12 and the other is 8x10. Time is of the essence - I've spent too much time trying to get this other company to do what I want.
Updates

Project Deadline Extended
Reason: Need more submissions.

I would like to shoot for Black, Red, White and a touch of Yellow for the colors of the signs.

Industry/Entity Type

Graphic Design

```html
<!DOCTYPE html>
<html lang="en">
<head>
<meta charset="utf-8">
<title>The Meadow at Briarwood Ridge – Now Selling Sign</title>
<link rel="stylesheet" href="https://fonts.googleapis.com/css2?family=Lato:wght@700;900&family=Archivo+Black&family=Arimo:wght@700&family=Baloo+2:wght@600&display=swap">
<style>
  :root {
    --sign-black: #141414;
    --sign-red: #c8102e;
    --accent-yellow: #f5c400;
    --paper: #ffffff;
    --shadow-grey: #808285;
  }
  * { margin: 0; padding: 0; box-sizing: border-box; }
  html, body {
    width: 1200px;
    height: 1000px;
    overflow: hidden;
    background: var(--paper);
  }
  .canvas {
    position: relative;
    width: 1200px;
    height: 1000px;
  }
  .sign-shadow {
    position: absolute;
    left: 256px;
    top: 104px;
    width: 672px;
    height: 840px;
    background: var(--shadow-grey);
  }
  .sign {
    position: absolute;
    left: 249px;
    top: 98px;
    width: 672px;
    height: 840px;
    background: var(--sign-black);
    overflow: hidden;
  }
  .sign-waves {
    position: absolute;
    left: 0;
    top: 0;
  }
  .centered {
    position: absolute;
    left: 0;
    width: 100%;
    text-align: center;
    white-space: nowrap;
    line-height: 1;
  }
  .project-name {
    position: absolute;
    left: 0;
    top: 0;
    width: 100%;
    height: 330px;
    font-family: "Lato", sans-serif;
    font-weight: 900;
    color: var(--paper);
  }
  .name-main {
    top: 152px;
    font-size: 104px;
    letter-spacing: 1px;
  }
  .name-sub {
    top: 282px;
    font-size: 35px;
    letter-spacing: 1.5px;
  }
  .product-line {
    top: 372px;
    font-family: "Lato", sans-serif;
    font-weight: 700;
    font-size: 43px;
    letter-spacing: 1px;
    color: var(--paper);
  }
  .builder-line {
    top: 428px;
    font-family: "Lato", sans-serif;
    font-weight: 700;
    font-size: 26px;
    letter-spacing: 0.5px;
    color: var(--paper);
  }
  .now-selling {
    top: 568px;
    font-family: "Archivo Black", sans-serif;
    font-size: 50px;
    color: var(--accent-yellow);
  }
  .phone {
    top: 638px;
    left: -28px;
    font-family: "Baloo 2", sans-serif;
    font-weight: 600;
    font-size: 84px;
    color: var(--paper);
    word-spacing: 22px;
  }
  .price-line {
    top: 748px;
    left: -32px;
    font-family: "Arimo", sans-serif;
    font-weight: 700;
    font-size: 45px;
    color: var(--accent-yellow);
  }
</style>
</head>
<body>
<main class="canvas">
  <div class="sign-shadow"></div>
  <section class="sign" aria-label="Now selling sign">
    <svg class="sign-waves" width="672" height="840" viewBox="249 98 672 840" aria-hidden="true">
      <path fill="var(--paper)" d="M249,740 C300,640 420,585 560,582 C680,580 760,612 850,588 C890,578 912,640 921,668 L921,938 L249,938 Z"/>
      <path fill="var(--sign-red)" d="M258,865 C248,800 262,730 312,676 C365,625 470,622 560,630 C660,640 720,648 780,628 C830,610 850,590 868,608 C895,650 902,760 860,830 C815,905 730,935 632,934 L249,938 L249,870 Z"/>
      <path fill="var(--sign-red)" d="M921,800 C895,870 840,920 755,938 L921,938 Z"/>
    </svg>

    <h1 class="project-name">
      <span class="centered name-main">The Meadow</span>
      <span class="centered name-sub">AT BRIARWOOD RIDGE</span>
    </h1>
    <p class="centered product-line">CUSTOM GARDEN HOMES</p>
    <p class="centered builder-line">BY HALVERN HOMES</p>

    <p class="centered now-selling">Now Selling</p>
    <p class="centered phone">555 014 2286</p>
    <p class="centered price-line">From the Low $200’s</p>
  </section>
</main>
</body>
</html>
```